BOOK COVER for THE IRONCLAD FOUNDER

I am publishing my first book and need to nail the cover. The cover should feature my picture as this is a major branding play.
TITLE: The Ironclad Founder.
SUBTITLE: Crafting A Steadfast Company Heritage.
BOOK DESCRIPTION: "The Ironclad Founder," presents a comprehensive approach to building resilient and sustainable businesses. The book emphasizes the inevitability of challenges in the business world and stresses the importance of resilience in facing adversity. It highlights the concept of "Ironcladding" a business, drawing inspiration from the safety glass used in car windshields, which doesn't shatter upon impact​​.

The book identifies two primary types of business owners: "TETHERED," who are overwhelmed and cannot take a break from their businesses without facing chaos, and "IRONCLAD" entrepreneurs, who have established systems and processes, clear goals, and can step away from their businesses without encountering problems​​. It raises critical questions about why some business owners become "TETHERED" while others achieve a "IRONCLAD" state and explores the transition from one to the other​​.

Dunmore points out that many well-intentioned business founders often lack a comprehensive roadmap or blueprint, leading to vulnerabilities in their businesses​​. Reflecting on his own journey from being a "TETHERED" to becoming "IRONCLAD," Dunmore shares insights from his experiences and the lessons he learned along the way​​.

The book addresses the legal aspects of businesses, an often overlooked area in entrepreneurial literature, providing readers with a roadmap and the necessary legal systems and structures to build a "IRONCLAD" business​​. This approach led to the development of Dunmore's Keystone Counsel Mentoring Plan and the Ironclad Method​​.

Dunmore encourages business owners to shift their paradigm, viewing lawyers as primary care providers for their businesses rather than turning to them only in emergencies​​. "The Ironclad Founder" is an invitation to make this paradigm shift and provides a roadmap for becoming a resilient and successful entrepreneur​​.

Target Market(s)

Small business owners from Start-up to $10 Million

Industry/Entity Type

Legal / Entrepreneurship

Font styles to use
Serif

Colors
0054AA
0677BA
7BADD7
CADEEF
E8F1F8

Requirements
Must have
• I am publishing my first book and need to nail the cover. The cover should feature my picture as this is a major branding play. The foreward has been written by Paul Vantrees. This needs to be included in the cover.

```html
<!DOCTYPE html>
<html lang="en">
<head>
<meta charset="utf-8">
<title>The Ironclad Founder – Cover Spread</title>
<link href="https://fonts.googleapis.com/css2?family=Bebas+Neue&family=Montserrat:wght@400;500;600;700&display=swap" rel="stylesheet">
<style>
  :root {
    --page-bg: #cfd0d2;
    --navy: #080e20;
    --navy-mid: #0b1a33;
    --cyan: #00d2e6;
    --blue: #0677ba;
    --deep-blue: #0054aa;
    --white: #ffffff;
    --body-text: #e8f1f8;
  }
  * { margin: 0; padding: 0; box-sizing: border-box; }
  html, body {
    width: 1200px; height: 1200px; overflow: hidden;
    background: var(--page-bg);
  }
  .spread {
    position: absolute; left: 40px; top: 213px;
    width: 1119px; height: 775px;
    background: var(--navy);
    overflow: hidden;
    font-family: "Montserrat", sans-serif;
    color: var(--white);
  }
  .back-glow {
    position: absolute; left: 120px; top: -80px; width: 260px; height: 160px;
    background: radial-gradient(ellipse at center, rgba(120,130,160,.45), transparent 70%);
  }
  .cover-photo {
    position: absolute; left: 600px; top: 0; width: 519px; height: 775px;
    background:
      radial-gradient(ellipse 260px 300px at 290px 230px, rgba(40,150,175,.75), transparent 75%),
      radial-gradient(ellipse 220px 260px at 300px 420px, rgba(48,82,150,.85), transparent 80%),
      linear-gradient(90deg, var(--navy) 0%, var(--navy-mid) 25%, #0d2a44 100%);
  }
  .title-line { font-family: "Bebas Neue", sans-serif; line-height: 1; text-transform: uppercase; white-space: nowrap; }
  .title-white { color: var(--white); }
  .grad-cyan-blue {
    background: linear-gradient(90deg, var(--cyan), var(--blue));
    -webkit-background-clip: text; background-clip: text; color: transparent;
  }
  .grad-blue-cyan {
    background: linear-gradient(90deg, var(--deep-blue), var(--cyan));
    -webkit-background-clip: text; background-clip: text; color: transparent;
  }
  .subtitle {
    font-weight: 600; text-transform: uppercase; text-align: center; line-height: 1.2;
  }

  /* back cover */
  .back-title { position: absolute; left: 48px; width: 420px; text-align: center; top: 42px; }
  .back-title .l1 { font-size: 55px; }
  .back-title .l2 { font-size: 70px; margin-top: -2px; }
  .back-subtitle { position: absolute; left: 48px; width: 420px; top: 157px; font-size: 13px; letter-spacing: 3.5px; }
  .back-copy {
    position: absolute; left: 49px; width: 420px; top: 218px;
    font-size: 9.2px; line-height: 12px; color: var(--body-text);
    text-align: justify; text-align-last: center;
  }
  .back-copy p { margin-bottom: 12px; }
  .isbn-box { position: absolute; left: 313px; top: 642px; width: 155px; height: 89px; background: var(--white); }

  /* spine */
  .spine-title {
    position: absolute; left: 543px; top: 60px;
    writing-mode: vertical-rl; font-size: 44px;
  }
  .spine-author {
    position: absolute; left: 550px; top: 591px;
    writing-mode: vertical-rl; white-space: nowrap;
    font-weight: 700; font-size: 17px; letter-spacing: 0.5px; line-height: 1;
  }

  /* front cover */
  .front-author {
    position: absolute; left: 627px; width: 470px; top: 24px; text-align: center;
    font-weight: 600; font-size: 41px; letter-spacing: 2px; line-height: 1; white-space: nowrap;
  }
  .front-author span {
    background: linear-gradient(90deg, var(--cyan), var(--deep-blue));
    -webkit-background-clip: text; background-clip: text; color: transparent;
  }
  .foreword {
    position: absolute; left: 627px; width: 470px; top: 66px; text-align: center;
    font-size: 10.5px; letter-spacing: 2.6px; text-transform: uppercase; font-weight: 500;
  }
  .front-title { position: absolute; left: 627px; width: 470px; top: 552px; text-align: center; }
  .front-title .l1 { font-size: 70px; }
  .front-title .l2 { font-size: 85px; margin-top: -2px; }
  .front-subtitle { position: absolute; left: 627px; width: 470px; top: 703px; font-size: 16px; letter-spacing: 4px; }

  .base-band {
    position: absolute; left: 0; bottom: 0; width: 100%; height: 12px;
    background: linear-gradient(90deg, var(--cyan), var(--deep-blue));
  }
</style>
</head>
<body>
  <main class="spread">
    <div class="back-glow"></div>

    <section class="back-cover">
      <h2 class="back-title">
        <div class="title-line l1"><span class="title-white">The </span><span class="grad-cyan-blue">Ironclad</span></div>
        <div class="title-line l2 grad-cyan-blue">Founder</div>
      </h2>
      <p class="subtitle back-subtitle">Crafting A Steadfast<br>Company Heritage.</p>
      <div class="back-copy">
        <p>"The Ironclad Founder," presents a comprehensive approach to building resilient and sustainable businesses. The book emphasizes the inevitability of challenges in the business world and stresses the importance of resilience in facing adversity. It highlights the concept of "Ironcladding" a business, drawing inspiration from the armored plating used on sea-going ships, which holds firm upon impact.</p>
        <p>The book identifies two primary types of business owners: "TETHERED," who are overwhelmed and cannot take a break from their businesses without facing chaos, and "IRONCLAD" entrepreneurs, who have established systems and processes, clear goals, and can step away from their businesses without encountering problems. It raises critical questions about why some business owners become "TETHERED" while others achieve an "IRONCLAD" state and explores the transition from one to the other.</p>
        <p>Dunmore points out that many well-intentioned business founders often lack a comprehensive roadmap or blueprint, leading to vulnerabilities in their businesses. Reflecting on his own journey from being "TETHERED" to becoming "IRONCLAD," Dunmore shares insights from his experiences and the lessons he learned along the way.</p>
        <p>The book addresses the legal aspects of businesses, an often overlooked area in entrepreneurial literature, providing readers with a roadmap and the necessary legal systems and structures to build an "IRONCLAD" business. This approach led to the development of Dunmore's Keystone Counsel Mentoring Plan and the Ironclad Method.</p>
        <p>Dunmore encourages business owners to shift their paradigm, viewing lawyers as primary care providers for their businesses rather than turning to them only in emergencies. "The Ironclad Founder" is an invitation to make this paradigm shift and provides a roadmap for becoming a resilient and successful entrepreneur.</p>
      </div>
      <div class="isbn-box"></div>
    </section>

    <section class="spine">
      <div class="title-line spine-title"><span class="title-white">The </span><span class="grad-cyan-blue">Ironclad Founder</span></div>
      <div class="spine-author">GRANT DUNMORE</div>
    </section>

    <section class="front-cover">
      <div class="cover-photo" role="img" aria-label="Portrait photograph of the author in a blue blazer with arms crossed, surrounded by floating shards of broken glass on a teal glow"></div>
      <p class="front-author"><span>GRANT DUNMORE</span></p>
      <p class="foreword">Foreward by Paul Vantrees</p>
      <h1 class="front-title">
        <div class="title-line l1"><span class="title-white">The </span><span class="grad-cyan-blue">Ironclad</span></div>
        <div class="title-line l2 grad-blue-cyan">Founder</div>
      </h1>
      <p class="subtitle front-subtitle">Crafting A Steadfast<br>Company Heritage.</p>
    </section>

    <div class="base-band"></div>
  </main>
</body>
</html>
```